Vantrelle Stationary Design

We're seeking a fresh and modern design for our stationery that captures the essence of our Real Estate brand. The current design, while functional, lacks visual appeal. We're looking for a more attractive and engaging design that showcases our professionalism and expertise in the real estate industry. I am attaching the current letter head and an image with a letter "P" as logo.

Target Market(s)

Real Estate Sales and Rentals

Industry/Entity Type

Real Estate

Requirements
Nice to have
• The owner seems to like the letter "P"

```html
<!DOCTYPE html>
<html lang="en">
<head>
<meta charset="utf-8">
<title>Vantrelle Stationery Set</title>
<link href="https://fonts.googleapis.com/css2?family=Nunito:wght@400;600;700&display=swap" rel="stylesheet">
<style>
  :root {
    --navy: #3f4a69;
    --navy-soft: #4a5577;
    --paper: #f5f5f5;
    --paper-white: #ffffff;
    --page-bg: #ffffff;
    --ink: #3f4a69;
    --faint: #e6e6e6;
  }
  * { box-sizing: border-box; margin: 0; padding: 0; }
  html, body {
    width: 1200px; height: 1200px; overflow: hidden;
    background: var(--page-bg);
    font-family: "Nunito", sans-serif;
    color: var(--ink);
  }
  .canvas { position: relative; width: 1200px; height: 1200px; }
  .sheet { position: absolute; overflow: hidden; }

  .wordmark {
    display: flex; align-items: center; gap: 9px;
    font-weight: 700; letter-spacing: 0.06em; text-transform: uppercase; white-space: nowrap;
  }
  .wordmark-name { display: flex; flex-direction: column; align-items: center; line-height: 1.15; }
  .wordmark-square { display: block; flex: none; }
  .faint-square { position: absolute; }

  /* folder cover */
  .folder { left: 96px; top: 191px; width: 465px; height: 599px; background: var(--navy); color: var(--paper-white); }
  .folder .wordmark { position: absolute; left: 0; right: 0; top: 268px; justify-content: center; font-size: 19px; color: var(--paper-white); }
  .folder .wordmark-square { width: 14px; height: 14px; background: var(--paper-white); }
  .folder-taglines { position: absolute; left: 0; right: 0; top: 323px; text-align: center; font-size: 12.5px; line-height: 1; }
  .folder-taglines li { list-style: none; margin-bottom: 9px; }
  .folder-taglines li:last-child { margin-top: 13px; }
  .folder .faint-square { right: 0; bottom: 0; width: 156px; height: 84px; background: var(--navy-soft); }

  /* letterhead */
  .letterhead { left: 646px; top: 191px; width: 466px; height: 599px; background: var(--paper); }
  .letterhead .wordmark { position: absolute; left: 57px; top: 83px; font-size: 12px; color: var(--ink); }
  .letterhead .wordmark-square { width: 10px; height: 10px; background: var(--navy); }
  .contact { position: absolute; left: 271px; top: 55px; font-size: 7.5px; letter-spacing: 0.04em; line-height: 11.5px; }
  .contact li { list-style: none; display: flex; gap: 7px; margin-bottom: 2px; }
  .contact svg { flex: none; width: 10px; height: 10px; margin-top: 1px; }
  .rule { position: absolute; left: 53px; width: 360px; top: 126px; height: 1px; background: var(--navy); }
  .letter { position: absolute; left: 57px; top: 142px; width: 352px; font-size: 11.3px; line-height: 13.1px; }
  .letter .label { font-size: 10.5px; }
  .letter .name { font-size: 15.5px; font-weight: 700; line-height: 17px; }
  .letter .role { font-weight: 700; font-size: 11px; }
  .recipient-details { margin-top: 8px; line-height: 13.5px; }
  .salutation { margin-top: 12px; font-weight: 700; }
  .body p { text-align: justify; text-align-last: left; }
  .body p + p { margin-top: 4px; }
  .sender { margin-top: 19px; }
  .signature { margin-top: 26px; width: 82px; border-top: 1px solid var(--navy); padding-top: 2px; font-size: 11px; }
  .letterhead .faint-square { right: 0; bottom: 0; width: 157px; height: 85px; background: var(--faint); }

  /* business card */
  .card { left: 118px; top: 827px; width: 421px; height: 189px; background: var(--paper); }
  .card .wordmark { position: absolute; left: 0; right: 0; top: 108px; justify-content: center; font-size: 12px; color: var(--ink); }
  .card .wordmark-square { width: 10px; height: 10px; background: var(--navy); }
  .card .faint-square { right: 0; bottom: 0; width: 94px; height: 50px; background: var(--faint); }

  /* envelope back */
  .envelope { left: 669px; top: 827px; width: 420px; height: 189px; background: var(--paper-white); }
  .envelope-flap { position: absolute; left: 0; top: 0; width: 64px; height: 189px; }
  .envelope .wordmark-square { position: absolute; left: 33px; top: 80px; width: 24px; height: 24px; background: var(--paper-white); }
  .envelope .faint-square { right: 0; bottom: 0; width: 94px; height: 50px; background: var(--faint); }
</style>
</head>
<body>
<main class="canvas">

  <section class="sheet folder" aria-label="Presentation folder cover">
    <div class="wordmark"><span class="wordmark-square"></span><span class="wordmark-name"><span>Vantrelle Property</span><span>Solutions</span></span></div>
    <ul class="folder-taglines">
      <li>-The Rental Leader</li>
      <li>-Vantrelle Property Solutions</li>
      <li>-Serving Boston’s Real Estate Needs for 25+ Years !</li>
    </ul>
    <span class="faint-square"></span>
  </section>

  <section class="sheet letterhead" aria-label="Letterhead">
    <div class="wordmark"><span class="wordmark-square"></span><span class="wordmark-name"><span>Vantrelle Property</span><span>Solutions</span></span></div>
    <ul class="contact">
      <li>
        <svg viewBox="0 0 10 10"><circle cx="5" cy="5" r="5" fill="#3f4a69"/><circle cx="5" cy="5" r="3" fill="none" stroke="#fff" stroke-width="0.7"/><path d="M2 5h6M5 2v6" stroke="#fff" stroke-width="0.6"/></svg>
        <span>vantrelleliving.com</span>
      </li>
      <li>
        <svg viewBox="0 0 10 10"><circle cx="5" cy="5" r="5" fill="#3f4a69"/><path d="M3.2 2.6l1 1-0.5 0.8a3 3 0 0 0 1.9 1.9l0.8-0.5 1 1-0.7 0.9c-2 -0.2-4.2-2.4-4.4-4.4z" fill="#fff"/></svg>
        <span>555-204-7318<br>555-204-7326</span>
      </li>
      <li>
        <svg viewBox="0 0 10 10"><circle cx="5" cy="5" r="5" fill="#3f4a69"/><path d="M5 2a2 2 0 0 1 2 2c0 1.4-2 3.8-2 3.8S3 5.4 3 4a2 2 0 0 1 2-2z" fill="#fff"/><circle cx="5" cy="4" r="0.7" fill="#3f4a69"/></svg>
        <span>48 Harborline Avenue,<br>Suite 2, Northfield, MA 02190</span>
      </li>
    </ul>
    <div class="rule"></div>

    <article class="letter">
      <div class="recipient">
        <p class="label">To.</p>
        <p class="name">Recipient's Name</p>
        <p class="role">Title</p>
        <div class="recipient-details">
          <p>Company Name</p>
          <p>Your Address Here</p>
          <p>Your Phone Number</p>
        </div>
      </div>
      <p class="salutation">Dear Sir</p>
      <div class="body">
        <p>There are many variations of passages of Lorem Ipsum available, but the majority have suffered alteration in some form, by injected humour, or randomised words which don't look even slightly believable. If you are going to use a passage of Lorem Ipsum, you need to be sure there isn't anything embarrassing hidden in the middle of text.</p>
        <p>All the Lorem Ipsum generators on the Internet tend to repeat predefined chunks as necessary, making this the first true generator on the Internet. It uses a dictionary of over 200 Latin words, combined with a handful of model sentence structures, to generate Lorem Ipsum which looks reasonable.</p>
        <p>The generated Lorem Ipsum is therefore always free from repetition, injected humour, or non-characteristic words etc</p>
      </div>
      <div class="sender">
        <p class="label">From.</p>
        <p class="name">Your Name</p>
        <p class="role">Your Title</p>
      </div>
      <p class="signature">Signature</p>
    </article>
    <span class="faint-square"></span>
  </section>

  <section class="sheet card" aria-label="Business card front">
    <div class="wordmark"><span class="wordmark-square"></span><span class="wordmark-name"><span>Vantrelle Property</span><span>Solutions</span></span></div>
    <span class="faint-square"></span>
  </section>

  <section class="sheet envelope" aria-label="Envelope back">
    <svg class="envelope-flap" viewBox="0 0 64 189" aria-hidden="true">
      <path d="M0 0 L57 5 Q64 6 64 14 L64 175 Q64 183 57 184 L0 189 Z" fill="#3f4a69"/>
    </svg>
    <span class="wordmark-square"></span>
    <span class="faint-square"></span>
  </section>

</main>
</body>
</html>
```